Quality Improvement Software for healthcare agencies needs a website.

VORTEL218 is a software for hospices and home health agencies to manage their Quality Assurance Performance Improvement programs to remain complaint with the standards set by Sanavox and the Bureau of Clinical Oversight. The web accessible software-as-a-service provides an easy, turn-key way for agencies to organize all the information they need to manage and track.

Coding

Coded - Design and coding required

Number of Pages Required

4 page

```html
<!DOCTYPE html>
<html lang="en">
<head>
<meta charset="utf-8">
<title>VORTEL218 — Closing The Quality Improvement Loop</title>
<link href="https://fonts.googleapis.com/css2?family=Sora:wght@600;700&family=Inter:wght@400;500;600&display=swap" rel="stylesheet">
<style>
:root{
  --navy:#0f2f4a;
  --text:#6d7a86;
  --mint:#e2efeb;
  --mint-2:#eef6f3;
  --yellow:#fde95a;
  --green:#4caf6e;
  --white:#ffffff;
  --line:#c9d3d8;
}
*{box-sizing:border-box;margin:0;padding:0}
html,body{width:1200px;height:5116px;overflow:hidden}
body{position:relative;background:var(--white);font-family:"Inter",sans-serif;color:var(--navy)}
.abs{position:absolute}
h1,h2,h3,.display{font-family:"Sora",sans-serif;font-weight:700;color:var(--navy)}
p{color:var(--text)}
.btn{display:inline-flex;align-items:center;gap:8px;border-radius:30px;font-weight:600;font-size:14px;text-decoration:none}
.btn-yellow{background:var(--yellow);color:var(--navy)}
.brand{font-family:"Sora",sans-serif;font-weight:700;font-size:20px;color:var(--navy);display:flex;align-items:center;gap:8px}
.brand .mark{width:16px;height:16px;background:var(--yellow);border-radius:3px}
.photo{border-radius:12px}

/* nav */
.nav-links{left:335px;top:30px;display:flex;gap:38px;font-size:14px;color:var(--navy)}
.nav-cta{left:1026px;top:20px;height:40px;padding:0 24px;font-size:13px}

/* hero */
.hero-title{left:75px;top:180px;font-size:52px;line-height:64px;letter-spacing:-1px;white-space:nowrap}
.hero-text{left:75px;top:345px;width:400px;font-size:15.5px;line-height:30px;color:#3c4b58}
.hero-start{left:75px;top:493px;height:48px;padding:0 30px;background:var(--navy);color:#fff}
.play{left:280px;top:493px;width:48px;height:48px;border-radius:50%;background:var(--yellow);display:flex;align-items:center;justify-content:center}
.watch{left:350px;top:508px;font-size:14px;font-weight:600;text-decoration:underline;color:var(--navy)}
.trust{left:646px;top:640px;width:242px;height:70px;background:#fff;border-radius:40px;display:flex;align-items:center;gap:14px;padding-left:10px;font-size:15px;line-height:19px;box-shadow:0 8px 24px rgba(0,0,0,.08)}
.trust .ic{width:52px;height:52px;border-radius:50%;background:var(--yellow);display:flex;align-items:center;justify-content:center}
.bubble{border-radius:50%;background:#fff;display:flex;align-items:center;justify-content:center;box-shadow:0 6px 20px rgba(0,0,0,.08)}

/* sections */
.sec-title{font-size:32px;line-height:40px}
.card-title{font-family:"Sora",sans-serif;font-weight:600;font-size:25px;line-height:31px;color:var(--navy)}
.small{font-size:13.5px;line-height:26px;color:var(--text)}
.icon-circle{width:76px;height:76px;border-radius:50%;background:var(--mint);display:flex;align-items:center;justify-content:center}
.card-box{background:#fff;border-radius:8px;box-shadow:0 10px 40px rgba(15,47,74,.1)}

.checks li{list-style:none;display:flex;align-items:center;gap:14px;font-size:14px;color:var(--text);height:35px}
.stat{width:380px;text-align:center}
.stat .num{font-family:"Sora",sans-serif;font-weight:700;font-size:40px;color:var(--navy)}
.stat .num span{color:var(--yellow)}
.stat .lbl{font-size:18px;color:var(--text);margin-top:4px}

.feat{background:#fff;border-radius:10px;box-shadow:0 10px 30px rgba(15,47,74,.08);padding:38px 38px}
.feat h3{font-family:"Inter",sans-serif;font-weight:500;font-size:20px;line-height:26px;margin-top:22px}

/* demo */
.field{position:absolute;left:56px;width:534px;height:36px;border:1.5px solid var(--line);background:rgba(255,255,255,.5);font-size:12px;color:#9aa5ad;padding:10px 14px}
.contact-row{display:flex;gap:20px}
.contact-row b{display:block;font-size:15px;font-weight:600;color:var(--navy)}
.contact-row span{font-size:14px;color:var(--text)}

/* news */
.post{width:320px}
.post .tag{display:inline-block;background:var(--mint);color:#6b8a7c;font-size:11px;padding:4px 14px;border-radius:14px;margin-top:30px}
.post h3{font-family:"Inter",sans-serif;font-weight:600;font-size:19.5px;line-height:26px;margin-top:10px;height:80px}
.post .btn{height:32px;padding:0 20px;font-size:12px;margin-top:16px}

/* footer */
.foot-card{left:24px;top:4700px;width:1152px;height:368px;background:#fff;border-radius:24px}
.foot-col h4{font-family:"Sora",sans-serif;font-weight:600;font-size:25px;margin-bottom:22px;color:var(--navy)}
.foot-col li{list-style:none;font-size:13px;color:var(--text);height:43px}
.social{display:flex;gap:26px;margin-top:18px}
.social i{display:block;width:22px;height:22px;border-radius:50%;background:var(--navy)}
</style>
</head>
<body>

<!-- hero background -->
<svg class="abs" style="left:0;top:0" width="1200" height="830" aria-hidden="true">
  <path d="M0 0H1200V795Q1200 825 1170 825H660Q620 825 590 795L560 730Q545 705 510 705H30Q0 705 0 675Z" fill="var(--mint)"/>
</svg>

<header>
  <div class="abs brand" style="left:50px;top:26px"><span class="mark"></span>VORTEL218</div>
  <nav class="abs nav-links"><span>Home</span><span>About</span><span>Products</span><span>Solutions</span><span>Pricing</span><span>Contact</span></nav>
  <a class="abs btn btn-yellow nav-cta">FREE DEMO</a>
</header>

<section class="hero">
  <h1 class="abs hero-title">Closing The Quality<br>Improvement Loop</h1>
  <p class="abs hero-text">The web accessible software-as-a-service provides an easy, turn-key way for agencies to organize all the information they need to manage and track.</p>
  <a class="abs btn hero-start">Let's Get Started</a>
  <div class="abs play"><svg width="16" height="16"><path d="M4 2L14 8L4 14Z" fill="var(--navy)"/></svg></div>
  <a class="abs watch">Watch Video</a>
  <div class="abs photo" role="img" aria-label="Smiling doctor in white coat holding a tablet" style="left:655px;top:90px;width:460px;height:735px;background:linear-gradient(180deg,#d5e6e0 0%,#f2f4f2 55%,#e2ece8 100%);border-radius:200px 200px 0 0"></div>
  <div class="abs bubble" style="left:1050px;top:140px;width:90px;height:90px">
    <svg width="40" height="36" fill="none" stroke="var(--green)" stroke-width="2"><path d="M4 32h32M8 30V20M16 30V14M24 30V18M32 30V8M6 16l10-8 8 6 10-10"/></svg>
  </div>
  <div class="abs bubble" style="left:710px;top:285px;width:64px;height:64px">
    <svg width="30" height="24" fill="none" stroke="var(--green)" stroke-width="2"><rect x="3" y="2" width="24" height="16" rx="2"/><path d="M1 22h28"/></svg>
  </div>
  <svg class="abs" style="left:1055px;top:255px" width="70" height="110" fill="none" stroke="var(--navy)" stroke-width="2"><path d="M4 104C50 90 30 50 56 8M46 14l10-8 6 12"/></svg>
  <div class="abs trust"><span class="ic"><svg width="24" height="26" fill="none" stroke="var(--navy)" stroke-width="2"><path d="M12 2L22 6V13C22 19 17 23 12 24C7 23 2 19 2 13V6Z"/><path d="M7 13l4 4 6-7"/></svg></span>100% trust and<br>reliability.</div>
</section>

<!-- partner badges -->
<div class="abs" role="img" aria-label="Lumora Care partner badge" style="left:50px;top:795px;width:180px;height:70px;background:#eceff1;border-radius:8px"></div>
<div class="abs" role="img" aria-label="Brightvale Clinics partner badge" style="left:348px;top:798px;width:160px;height:62px;background:#f3e6e4;border-radius:8px"></div>

<!-- software section -->
<h2 class="abs sec-title" style="left:56px;top:1015px;width:460px">Software For Hospices And Home Health Agencies</h2>
<p class="abs small" style="left:740px;top:1015px;width:400px">Lorem ipsum dolor sit amet, consectetur tempoesed uted adipiscing elit, sed do eiusmod tempor incididunt labore et dolore magna aliqua ut commodo conse.</p>

<div class="abs" style="left:94px;top:1232px;width:280px">
  <div class="icon-circle"><svg width="40" height="40" fill="none" stroke="var(--green)" stroke-width="2"><circle cx="20" cy="20" r="12"/><path d="M20 13l2 5h5l-4 3 2 5-5-3-5 3 2-5-4-3h5z"/></svg></div>
  <h3 class="card-title" style="margin-top:34px">Maximize Quality And Performance</h3>
  <p class="small" style="margin-top:16px">Lorem ipsum dolor sit amet, commodo conse consecteturet deus adipiscing elit, sed do eiusmod tempor ut.</p>
  <svg style="margin-top:28px" width="24" height="14" fill="none" stroke="var(--navy)" stroke-width="1.8"><path d="M0 7h22M16 1l6 6-6 6"/></svg>
</div>
<div class="abs" style="left:466px;top:1232px;width:280px">
  <div class="icon-circle"><svg width="40" height="40" fill="none" stroke="var(--green)" stroke-width="2"><rect x="11" y="8" width="18" height="26" rx="2"/><path d="M16 16h8M16 22h8M16 28h5"/></svg></div>
  <h3 class="card-title" style="margin-top:34px">Reduce Burden On Your Care Providers</h3>
  <p class="small" style="margin-top:16px">Lorem ipsum dolor sit amet, commodo conse consecteturet deus adipiscing elit, sed do eiusmod tempor ut.</p>
  <svg style="margin-top:28px" width="24" height="14" fill="none" stroke="var(--navy)" stroke-width="1.8"><path d="M0 7h22M16 1l6 6-6 6"/></svg>
</div>
<div class="abs card-box" style="left:800px;top:1170px;width:343px;height:412px;padding:36px 38px">
  <div class="icon-circle"><svg width="40" height="40" fill="none" stroke="var(--green)" stroke-width="2"><rect x="9" y="8" width="22" height="26" rx="2"/><path d="M14 15h12M14 20h12M14 25h7"/><circle cx="27" cy="29" r="4"/></svg></div>
  <h3 class="card-title" style="margin-top:32px">Improve Your Bottom Line</h3>
  <p class="small" style="margin-top:16px">Lorem ipsum dolor sit amet, commodo conse consecteturet deus adipiscing elit, sed do eiusmod tempor ut.</p>
  <svg style="margin-top:30px" width="24" height="14" fill="none" stroke="var(--navy)" stroke-width="1.8"><path d="M0 7h22M16 1l6 6-6 6"/></svg>
</div>

<!-- about -->
<div class="abs" style="left:56px;top:1790px;width:552px;height:425px;background:var(--mint);border-radius:18px"></div>
<div class="abs" role="img" aria-label="Smiling businesswoman pointing at a dashboard" style="left:120px;top:1755px;width:340px;height:460px;background:linear-gradient(180deg,#e6e3df,#d3d7da);border-radius:170px 170px 0 0"></div>
<div class="abs" role="img" aria-label="Software dashboard screen with charts" style="left:410px;top:1735px;width:252px;height:172px;background:#fff;border-radius:14px;box-shadow:0 8px 24px rgba(0,0,0,.1);padding:14px"><div style="width:100%;height:100%;border:3px solid var(--navy);border-radius:10px;background:linear-gradient(135deg,#eef6f3,#dff0ea)"></div></div>
<div class="abs" style="left:38px;top:1838px;width:150px;height:46px;background:#fff;border-radius:10px;box-shadow:0 6px 18px rgba(0,0,0,.08);display:flex;align-items:center;gap:4px;padding-left:14px">
  <i style="width:22px;height:22px;border-radius:50%;background:#c9b9a8"></i><i style="width:22px;height:22px;border-radius:50%;background:#a8b4c0"></i><i style="width:22px;height:22px;border-radius:50%;background:#bfa8a0"></i><i style="width:22px;height:22px;border-radius:50%;background:#9fb0a8"></i><i style="width:22px;height:22px;border-radius:50%;background:var(--navy)"></i>
</div>
<svg class="abs" style="left:100px;top:1905px" width="70" height="70" fill="none" stroke="var(--navy)" stroke-width="2"><path d="M60 62C30 60 14 40 10 6M2 14l8-8 8 8"/></svg>

<h2 class="abs sec-title" style="left:757px;top:1790px;font-size:38px">About VORTEL218</h2>
<p class="abs small" style="left:757px;top:1862px;width:380px">Lorem ipsum dolor sit amet, consectetur adipiscing elit, sed do eiusmod tempor incididunt ut labore et dolore magna aliqua. Ut enim ad minim.</p>
<ul class="abs checks" style="left:757px;top:1965px">
  <li><svg width="16" height="12" fill="none" stroke="var(--green)" stroke-width="2"><path d="M1 6l5 5 9-10"/></svg>Outstanding communication.</li>
  <li><svg width="16" height="12" fill="none" stroke="var(--green)" stroke-width="2"><path d="M1 6l5 5 9-10"/></svg>Superior management expertise.</li>
  <li><svg width="16" height="12" fill="none" stroke="var(--green)" stroke-width="2"><path d="M1 6l5 5 9-10"/></svg>Email and live chat support.</li>
</ul>
<a class="abs btn btn-yellow" style="left:757px;top:2098px;height:52px;padding:0 32px">More About <svg width="16" height="10" fill="none" stroke="var(--navy)" stroke-width="1.6"><path d="M0 5h14M10 1l4 4-4 4"/></svg></a>

<!-- stats -->
<div class="abs stat" style="left:36px;top:2305px"><div class="num">1,465<span>+</span></div><div class="lbl">Happy Customers</div></div>
<div class="abs stat" style="left:410px;top:2305px"><div class="num">5K<span>+</span></div><div class="lbl">Software Installs</div></div>
<div class="abs stat" style="left:784px;top:2305px"><div class="num">25<span>+</span></div><div class="lbl">Years Experience</div></div>

<!-- features -->
<h2 class="abs sec-title" style="left:56px;top:2520px;font-size:38px">Features &amp; Benefits</h2>
<p class="abs small" style="left:56px;top:2594px;width:380px">Lorem ipsum dolor sit amet, consectetur adipiscing elit, sed do eiusmod tempor incididunt ut labore.</p>
<a class="abs btn btn-yellow" style="left:56px;top:2666px;height:50px;padding:0 32px">More Service <svg width="16" height="10" fill="none" stroke="var(--navy)" stroke-width="1.6"><path d="M0 5h14M10 1l4 4-4 4"/></svg></a>

<svg class="abs" style="left:582px;top:2500px" width="572" height="572" aria-hidden="true">
  <path d="M30 0H250Q275 0 290 20L300 38H540Q560 38 560 58V250Q572 250 572 270V545Q572 570 548 570H30Q0 570 0 545V40Q0 0 30 0Z" fill="var(--mint-2)"/>
</svg>
<div class="abs feat" style="left:608px;top:2527px;width:250px;height:219px">
  <svg width="48" height="40" fill="none" stroke="var(--green)" stroke-width="2"><rect x="8" y="4" width="32" height="22" rx="2"/><path d="M14 20v-6M20 20v-10M26 20v-4M32 20v-8M2 34h44"/></svg>
  <h3>Centralize Quality Program Data</h3>
  <svg style="margin-top:10px" width="22" height="12" fill="none" stroke="var(--text)" stroke-width="1.5"><path d="M0 6h20M15 1l5 5-5 5"/></svg>
</div>
<div class="abs feat" style="left:884px;top:2563px;width:247px;height:219px">
  <svg width="46" height="46" fill="none" stroke="var(--green)" stroke-width="2"><circle cx="23" cy="23" r="20"/><path d="M23 10v13l8 6"/></svg>
  <h3>Spend Less Time On Compliance</h3>
  <svg style="margin-top:10px" width="22" height="12" fill="none" stroke="var(--text)" stroke-width="1.5"><path d="M0 6h20M15 1l5 5-5 5"/></svg>
</div>
<div class="abs feat" style="left:608px;top:2776px;width:250px;height:244px">
  <svg width="48" height="48" fill="none" stroke="var(--green)" stroke-width="2"><circle cx="24" cy="8" r="5"/><path d="M24 13v10M10 30l14-7 14 7"/><circle cx="10" cy="36" r="5"/><circle cx="38" cy="36" r="5"/><circle cx="24" cy="40" r="5"/></svg>
  <h3>Improve Performance And Star Rating</h3>
  <svg style="margin-top:10px" width="22" height="12" fill="none" stroke="var(--text)" stroke-width="1.5"><path d="M0 6h20M15 1l5 5-5 5"/></svg>
</div>
<div class="abs feat" style="left:884px;top:2812px;width:247px;height:218px">
  <svg width="40" height="46" fill="none" stroke="var(--green)" stroke-width="2"><rect x="6" y="20" width="28" height="22" rx="2"/><path d="M12 20v-6a8 8 0 0116 0v6"/></svg>
  <h3>Data Security And Privacy</h3>
  <svg style="margin-top:10px" width="22" height="12" fill="none" stroke="var(--text)" stroke-width="1.5"><path d="M0 6h20M15 1l5 5-5 5"/></svg>
</div>

<!-- demo -->
<section class="abs" style="left:0;top:3170px;width:1200px;height:418px;background:linear-gradient(90deg,#fbf5c8 0%,#eef5f1 30%,var(--mint) 100%)">
  <div class="field" style="top:64px">Name</div>
  <div class="field" style="top:110px">Phone</div>
  <div class="field" style="top:157px">Email</div>
  <div class="field" style="top:203px;height:88px">Message</div>
  <div class="abs" style="left:56px;top:304px;width:534px;height:36px;background:var(--yellow);font-size:13px;font-weight:600;display:flex;align-items:center;justify-content:center">Request A Demo</div>
  <h2 class="abs sec-title" style="left:715px;top:116px;font-size:36px;white-space:nowrap">Request A Free Demo</h2>
  <div class="abs contact-row" style="left:715px;top:196px">
    <svg width="32" height="32" fill="none" stroke="#8aa39a" stroke-width="1.5"><path d="M2 6l9-3 10 3 9-3v23l-9 3-10-3-9 3zM11 3v23M21 6v23"/></svg>
    <div><b>Our Address</b><span>Harlow Lane No.42, Westbury.</span></div>
  </div>
  <div class="abs contact-row" style="left:715px;top:264px">
    <svg width="32" height="32" fill="none" stroke="#8aa39a" stroke-width="1.5"><path d="M6 3l6 1 2 7-4 3c2 4 5 7 9 9l3-4 7 2 1 6c-1 2-3 3-5 3C13 29 3 19 2 8c0-2 2-4 4-5z"/></svg>
    <div><b>Contact Info</b><span>(555) 014-2290</span></div>
  </div>
</section>

<!-- news -->
<h2 class="abs sec-title" style="left:0;top:3645px;width:1200px;text-align:center;font-size:40px">Our Latest News &amp; Blog</h2>
<article class="abs post" style="left:94px;top:3762px">
  <div class="photo" role="img" aria-label="Colleagues working together at a computer" style="height:246px;border-radius:4px;background:linear-gradient(135deg,#7d8c98,#c7cfd4)"></div>
  <span class="tag">Uncategorized</span>
  <h3>Your Side Hustle Success Begins With Finding The Money</h3>
  <a class="btn btn-yellow">Read More <svg width="12" height="8" fill="none" stroke="var(--navy)" stroke-width="1.4"><path d="M0 4h11M8 1l3 3-3 3"/></svg></a>
</article>
<article class="abs post" style="left:440px;top:3762px">
  <div class="photo" role="img" aria-label="Team reviewing a tablet in an office" style="height:246px;border-radius:4px;background:linear-gradient(135deg,#9a8f86,#d6d2cc)"></div>
  <span class="tag">Uncategorized</span>
  <h3>4 Tactics To Boost Your Team's Collaboration In A Remote World</h3>
  <a class="btn btn-yellow">Read More <svg width="12" height="8" fill="none" stroke="var(--navy)" stroke-width="1.4"><path d="M0 4h11M8 1l3 3-3 3"/></svg></a>
</article>
<article class="abs post" style="left:787px;top:3762px">
  <div class="photo" role="img" aria-label="Group meeting around a laptop" style="height:246px;border-radius:4px;background:linear-gradient(135deg,#a88868,#d9d3cc)"></div>
  <span class="tag">Uncategorized</span>
  <h3>5 Steps To Making A Successful Career Pivot In Your Fifties</h3>
  <a class="btn btn-yellow">Read More <svg width="12" height="8" fill="none" stroke="var(--navy)" stroke-width="1.4"><path d="M0 4h11M8 1l3 3-3 3"/></svg></a>
</article>

<!-- cta -->
<svg class="abs" style="left:0;top:4312px" width="1200" height="804" aria-hidden="true">
  <path d="M0 140Q0 110 30 110H520Q555 110 580 70L610 25Q625 0 660 0H1200V804H0Z" fill="var(--mint)"/>
</svg>
<h2 class="abs display" style="left:0;top:4500px;width:1200px;text-align:center;font-size:44px;line-height:62px;font-weight:600">Are You Ready? Claim Your Free<br>Account Now.</h2>

<footer>
  <div class="abs foot-card"></div>
  <div class="abs brand" style="left:82px;top:4800px;font-size:26px"><span class="mark" style="width:20px;height:20px"></span>VORTEL218</div>
  <p class="abs" style="left:80px;top:4850px;width:240px;font-size:13px;line-height:22px;color:var(--navy)">Closing The Quality Improvement Loop</p>
  <div class="abs foot-col" style="left:345px;top:4772px"><h4>Menu</h4><ul><li>Home</li><li>About</li><li>Services</li><li>Contact</li></ul></div>
  <div class="abs foot-col" style="left:609px;top:4772px"><h4>Services</h4><ul><li>Quality Improvement</li><li>Data Security</li><li>Save Time</li><li>Maximize Quality</li></ul></div>
  <div class="abs foot-col" style="left:873px;top:4772px;width:240px"><h4>Our Address</h4>
    <p style="font-size:13px;line-height:22px">Harlow Lane No.42, 50218, Westbury.</p>
    <p style="font-size:13px;margin-top:18px">(555) 014-2290</p>
    <div class="social"><i></i><i></i><i></i></div>
  </div>
  <p class="abs" style="left:0;top:5094px;width:1200px;text-align:center;font-size:12px;color:var(--navy)">© 2023 VORTEL218 All Rights Reserved</p>
</footer>

</body>
</html>
```